Stonefield Partners - Web Design

I have recently established a business called Stonefield Partners. The business is focused on providing property developers with project financing solutions. This is not a real estate website so please do not provide such pics or design. I provide financial solutions.

I have been in the financial markets for the past 20 years covering all asset classes from trading through to portfolio management, structuring and business development. The majority of this time was spent with building new business and expanding into new opportunities.

This is a start-up business so there isn't much content at this stage. Therefore, its all about first impressions. I want a design that portray confidence; and that I can deliver a workable solution. It must provide the perception of sophistication, innovation, yet simplistic so its not trying to deceive/hide something. Most importantly it must give the Client a sense of trust and reliability.

I would like to have the website portray my depth of experience in providing financing solutions and consultancy services in achieving the investment objectives. However, I would like to avoid looking like a one man band. I do have access to resources just not directly employed by the company.

Anyway, I hope this is enough to at least wet your appetite. I recently had a logo created on ArtHive that should set the theme/style of the website

Project Deadline Extended
Reason: Increase time to allow web designer/developer more time to understand the style I am after.

All, Thank you for your current designs. I am based in Singapore, however, I am currently traveling today but will respond by later tonight or tomorrow. Rolf

All, A general observation. Please do not include photos of houses, architectural drawings or images that portal construction or real estate. This implies I am either a property agent or in some way directly involve in selling property...very misleading. Remember, I am involved in provide financial solutions not selling property. Rolf

All, Please avoid using numerous people within the site as it may represent that my business has a large number of staff when in fact its only me. However, I also don't want to look like a "one man band". So be balanced on using people - I am not sure I want people at all. Thanks Rolf

Some designers are not reading the brief or previous messages. If you do more then once I will simply not comment and eliminate ask not to provide any more.

please stop using pictures and/or logos that imply - I manage their money - I protect their money - I grow their money - I offer homes loans - that I do house calls with individuals (i.e no couples shaking heads with a guy) - no house pictures or symbols i.e. it looks like a property website - I have a large organisation (i.e. team of people) If any design include the above I will eliminate it REMEMBER: I am providing innovative financial solutions - NOT asset/fund manager, bank manager or real estate manager thank you

All Please be creative and innovative with your pics. Also ensure you have the rights to use the pics. I have seen basic stock photos being used and again have not read by brief or previous comments. For instance, they use the words "sustainable growth" in google and click on images and you will see most of the images being used. these will be eliminated instantly and not asked to return.

Please, if you use the name of the Company as a Label or Statement can please ensure it remains in the same style as the Logo, i.e. all Caps Large with small.

All, I have decided that I don't want to have people in the main pic on the front page so please provide other inspirational pics. Thanks

guys I found a coffee advert whilst in Vietnam. I like the colour selection and thought it would be inspirational.i ahve added it yo my bried f

```html
<!DOCTYPE html>
<html lang="en">
<head>
<meta charset="utf-8">
<title>Stonefield Partners</title>
<link href="https://fonts.googleapis.com/css2?family=Exo+2:wght@300;400;500;600&display=swap" rel="stylesheet">
<style>
:root{
  --gold:#b8982f;
  --ink:#222;
  --text:#555;
  --muted:#777;
  --header-bg:#ebebeb;
  --band-blue:#d9eefb;
  --feature-grey:#e6e6e6;
  --footer-bg:#363a40;
  --footer-text:#d8d8d8;
  --white:#fff;
}
*{margin:0;padding:0;box-sizing:border-box}
html,body{width:1200px;height:2544px;overflow:hidden}
body{font-family:"Exo 2",sans-serif;color:var(--text);background:var(--white);position:relative}
h2,h3,h4{font-weight:400}
.abs{position:absolute}

/* header */
.site-header{position:absolute;left:0;top:0;width:1200px;height:174px;background:var(--header-bg);border-bottom:4px solid var(--gold)}
.call{left:102px;top:40px;font-size:15px;color:#444;line-height:21px}
.call .phone{color:var(--gold);display:block;text-align:right;padding-right:14px}
.call-icon{left:372px;top:44px}
.brand{position:absolute;left:448px;top:26px;width:304px;height:84px;display:flex;align-items:center;justify-content:center;gap:14px}
.brand-mark{width:60px;height:60px;background:var(--gold);flex:none}
.brand-name{color:#222;font-weight:600;line-height:1;text-align:center}
.brand-name .big{font-size:32px;letter-spacing:2px;display:block}
.brand-name .small{font-size:14px;letter-spacing:6px;display:block;margin-top:5px}
.email-icon{left:806px;top:44px}
.email{left:840px;top:40px;font-size:15px;color:#444;line-height:21px}
.email span{color:var(--gold);display:block}
.main-nav{left:0;top:130px;width:1200px;display:flex;justify-content:center;gap:30px;font-size:15px;color:#222;font-weight:500}

/* hero */
.hero{left:0;top:178px;width:1200px;height:608px;background:linear-gradient(100deg,#6f7b86 0%,#56616d 35%,#2f3a4a 65%,#1c2535 100%)}
.hero-content{left:0;top:178px;width:1200px;height:608px;text-align:center;color:var(--white)}
.hero-mark{position:absolute;left:584px;top:180px;width:34px;height:34px;background:var(--gold)}
.hero-kicker{position:absolute;top:290px;width:100%;font-size:28px;font-weight:500;letter-spacing:1px}
.hero-title{position:absolute;top:320px;width:100%;font-size:60px;font-weight:600;letter-spacing:1px}
.hero-start{position:absolute;top:468px;width:100%;font-size:17px}
.hero-chevron{position:absolute;left:586px;top:496px}
.hero-dots{position:absolute;top:568px;left:528px;display:flex;gap:8px}
.hero-dots i{width:24px;height:24px;border-radius:50%;background:rgba(255,255,255,.45);display:block}
.hero-dots i.on{background:transparent;border:4px solid var(--white)}

/* welcome */
.welcome-title{left:0;top:852px;width:1200px;text-align:center;font-size:32px;color:var(--ink)}
.gold-rule{height:4px;background:var(--gold)}
.welcome-rule{left:582px;top:910px;width:38px}
.welcome-text{left:150px;width:900px;text-align:center;font-size:14.5px;line-height:23px;color:#555}

/* stat band */
.stat-band{left:0;top:1215px;width:1200px;height:178px;background:var(--band-blue);overflow:hidden}
.stat-globe{position:absolute;right:90px;top:-10px;width:200px;height:200px;border-radius:50%;background:radial-gradient(circle,#c3dcee 0%,rgba(195,220,238,0) 70%)}
.stat-title{position:absolute;left:85px;top:26px;font-size:27px;color:var(--ink)}
.stat-text{position:absolute;left:88px;top:72px;width:860px;font-size:14.5px;line-height:22px;color:#333}
.stat-link{position:absolute;left:88px;top:124px;font-size:14px;color:#2b7bb9}

/* features */
.features{left:0;top:1393px;width:1200px;height:374px;background:var(--feature-grey)}
.feature{position:absolute;top:66px;width:290px}
.feature h3{margin-top:40px;font-size:17px;font-weight:500;color:#222}
.feature .gold-rule{width:88px;margin-top:16px;height:2px}
.feature p{margin-top:24px;font-size:14.5px;line-height:22px;color:#555}
.feature h3.gold{color:var(--gold)}
.feature .lead{font-size:19px;line-height:23px;color:#444}
.feature .mail{margin-top:10px;font-size:15px;color:#555}

/* testimonials */
.testi-title{left:0;top:1826px;width:1200px;text-align:center;font-size:34px;color:var(--ink)}
.testi-sub{left:0;top:1872px;width:1200px;text-align:center;font-size:17px;color:#666}
.testi-card{position:absolute;top:1929px;width:237px;height:117px;background:var(--white);border:1px solid #ddd;padding:12px 14px;font-size:13px;line-height:19px;text-align:center;color:#666}
.testi-card::after{content:"";position:absolute;left:110px;bottom:-9px;width:16px;height:16px;background:var(--white);border-right:1px solid #ddd;border-bottom:1px solid #ddd;transform:rotate(45deg)}
.avatar{position:absolute;top:2096px;width:60px;height:60px;border-radius:50%;background:linear-gradient(#d8cfc7,#a8a099);border:3px solid #e2e2e2}
.client{position:absolute;top:2164px;width:200px;text-align:center;font-size:16px;color:#333}
.arrow{position:absolute;top:2040px}

/* footer */
.site-footer{left:0;top:2255px;width:1200px;height:289px;background:var(--footer-bg);border-top:4px solid var(--gold);color:var(--footer-text)}
.foot-col{position:absolute;top:44px;font-size:13.5px;line-height:20px}
.foot-col h4{font-size:15.5px;font-weight:500;color:var(--white);margin-bottom:10px}
.social{position:absolute;top:42px;width:40px;height:40px;border:2px solid var(--white)}
.legal{position:absolute;top:250px;font-size:11.5px;color:var(--footer-text)}
</style>
</head>
<body>

<header class="site-header">
  <div class="abs call">I CASE OF ANY QUESTIONS, PLEASE CALL:<span class="phone">+111-555-0190</span></div>
  <svg class="abs call-icon" width="18" height="22" viewBox="0 0 18 22"><path d="M4 2 L8 6 L6 9 Q8 14 12 16 L15 14 L18 18 L15 21 Q4 18 1 5 Z" fill="var(--gold)"/></svg>
  <div class="brand">
    <div class="brand-mark"></div>
    <div class="brand-name"><span class="big">STONEFIELD</span><span class="small">PARTNERS</span></div>
  </div>
  <svg class="abs email-icon" width="24" height="18" viewBox="0 0 24 18"><rect width="24" height="18" fill="var(--gold)"/><path d="M1 1 L12 10 L23 1" stroke="#fff" stroke-width="2" fill="none"/></svg>
  <div class="abs email">EMAIL:<span>INFO@STONEFIELDPARTNERS.COM</span></div>
  <nav class="abs main-nav"><span>HOME</span><span>ABOUT US</span><span>SERVICES</span><span>FUNDING OPTIONS</span><span>CONTACT US</span></nav>
</header>

<div class="abs hero" role="img" aria-label="Hero photograph: two businessmen reviewing documents in an office"></div>
<div class="abs hero-content">
  <div class="hero-mark"></div>
  <div class="hero-kicker">LOREM IPSUM DOLOR SIT AMET</div>
  <div class="hero-title">CONSECTETUR ADIPISCING ELIT</div>
  <div class="hero-start">START</div>
  <svg class="hero-chevron" width="28" height="28" viewBox="0 0 28 28"><circle cx="14" cy="14" r="12.5" fill="none" stroke="#fff" stroke-width="2"/><path d="M8 11 L14 17 L20 11" fill="none" stroke="#fff" stroke-width="2.5"/></svg>
  <div class="hero-dots"><i class="on"></i><i></i><i></i><i></i><i></i></div>
</div>

<h2 class="abs welcome-title">WELCOME TO STONEFIELD PARTNERS</h2>
<div class="abs gold-rule welcome-rule"></div>
<p class="abs welcome-text" style="top:954px">Lorem ipsum dolor sit amet, consectetur adipiscing elit, sed do eiusmod tempor incididunt ut labore et dolore magna aliqua. Ut enim ad minim veniam, quis nostrud exercitation ullamco laboris nisi ut aliquip ex ea commodo consequat. Duis aute irure dolor in reprehenderit in voluptate velit esse cillum dolore eu fugiat nulla pariatur. Excepteur sint occaecat cupidatat non proident, sunt in culpa qui officia deserunt mollit anim id est laborum.</p>
<p class="abs welcome-text" style="top:1072px">Lorem ipsum dolor sit amet, consectetur adipiscing elit, sed do eiusmod tempor incididunt ut labore et dolore magna aliqua. Ut enim ad minim veniam, quis nostrud exercitation ullamco laboris nisi ut aliquip ex ea commodo consequat. Duis aute irure dolor in reprehenderit in voluptate velit esse cillum dolore eu fugiat nulla pariatur. Excepteur sint occaecat cupidatat non proident, sunt in culpa qui officia deserunt mollit anim id est laborum.</p>

<section class="abs stat-band">
  <div class="stat-globe" role="img" aria-label="Faint globe illustration"></div>
  <h2 class="stat-title">OVER $700 MILLION LENT TO SMALL BUSINESSES GLOBALLY</h2>
  <p class="stat-text">Lorem ipsum dolor sit amet, consectetur adipiscing elit, sed do eiusmod tempor incididunt ut labore et dolore magna aliqua. Ut enim ad minim veniam, quis nostrud exercitation ullamco laboris nisi ut aliquip ex ea commodo consequat.</p>
  <span class="stat-link">Learn more</span>
</section>

<section class="abs features">
  <div class="feature" style="left:108px">
    <svg width="34" height="40" viewBox="0 0 34 40"><path d="M12 4 L22 4 L18 11 L16 11 Z" fill="none" stroke="#333" stroke-width="2"/><path d="M15 11 Q2 22 8 36 L26 36 Q32 22 19 11 Z" fill="none" stroke="#333" stroke-width="2"/><text x="17" y="30" font-size="12" text-anchor="middle" fill="#333" font-family="Exo 2, sans-serif">$</text></svg>
    <h3>FINANCING</h3>
    <div class="gold-rule"></div>
    <p>Lorem ipsum dolor sit amet, consectetur adipiscing elit, sed do eiusmod tempor incididunt ut labore et dolore magna aliqua.</p>
  </div>
  <div class="feature" style="left:464px">
    <svg width="40" height="40" viewBox="0 0 40 40"><path d="M4 18 L20 6 L36 18" fill="none" stroke="#333" stroke-width="2"/><rect x="8" y="18" width="24" height="18" fill="none" stroke="#333" stroke-width="2"/><path d="M14 22h4v4h-4zM22 22h4v4h-4zM14 29h4v4h-4zM22 29h4v4h-4z" fill="#333"/></svg>
    <h3>FORECLOSURE SERVICES</h3>
    <div class="gold-rule"></div>
    <p>Lorem ipsum dolor sit amet, consectetur adipiscing elit, sed do eiusmod tempor incididunt ut labore et dolore magna aliqua.</p>
  </div>
  <div class="feature" style="left:818px">
    <svg width="40" height="40" viewBox="0 0 40 40"><rect x="4" y="4" width="18" height="32" rx="2" fill="none" stroke="#333" stroke-width="2"/><rect x="16" y="16" width="20" height="14" fill="#fff" stroke="#333" stroke-width="2"/><path d="M16 16 L26 24 L36 16" fill="none" stroke="#333" stroke-width="2"/></svg>
    <h3 class="gold">ALLOW 24HRS. FOR RESPONSE.</h3>
    <div class="gold-rule"></div>
    <p class="lead">All Serious inquiries must be in writing.</p>
    <p class="mail">inquiry@stonefieldpartners.com</p>
  </div>
</section>

<h2 class="abs testi-title">CLIENTS TESTIMONIALS</h2>
<p class="abs testi-sub">WHAT DOES OUR CLIENTS SAY</p>

<svg class="arrow" style="left:88px" width="22" height="42" viewBox="0 0 22 42"><path d="M20 2 L2 21 L20 40" fill="none" stroke="#ccc" stroke-width="2"/></svg>
<svg class="arrow" style="left:1092px" width="22" height="42" viewBox="0 0 22 42"><path d="M2 2 L20 21 L2 40" fill="none" stroke="#ccc" stroke-width="2"/></svg>

<div class="testi-card" style="left:176px">Lorem ipsum dolor sit amet, consectetur adipiscing elit, sed do eiusmod tempor incididunt ut labore et dolore magna aliqua.</div>
<div class="testi-card" style="left:482px">Lorem ipsum dolor sit amet, consectetur adipiscing elit, sed do eiusmod tempor incididunt ut labore et dolore magna aliqua.</div>
<div class="testi-card" style="left:796px">Lorem ipsum dolor sit amet, consectetur adipiscing elit, sed do eiusmod tempor incididunt ut labore et dolore magna aliqua.</div>

<div class="avatar" style="left:264px" role="img" aria-label="Client portrait photo"></div>
<div class="avatar" style="left:570px" role="img" aria-label="Client portrait photo"></div>
<div class="avatar" style="left:884px" role="img" aria-label="Client portrait photo"></div>
<div class="client" style="left:194px">Mark Halden</div>
<div class="client" style="left:500px">Owen Pratley</div>
<div class="client" style="left:814px">Mark Halden</div>

<footer class="abs site-footer">
  <div class="foot-col" style="left:85px"><h4>Funding Hub</h4>Small business loans<br>Commercial loan comparison</div>
  <div class="foot-col" style="left:333px"><h4>How it works</h4>Invest in small business<br>FAQ</div>
  <div class="foot-col" style="left:545px"><h4>About us</h4>Our company<br>Team<br>Careers<br>Blog<br>Newsroom</div>
  <div class="foot-col" style="left:693px"><h4>Get in touch</h4>support@stonefieldpartners.com<br>111-555-0190<br>Contact us</div>
  <div class="social" style="left:965px"></div>
  <div class="social" style="left:1024px"></div>
  <div class="social" style="left:1081px"></div>
  <div class="legal" style="left:85px">COPYRIGHT ©2015 STONEFIELD PARTNERS.&nbsp; ALL RIGHTS RESERVED.</div>
  <div class="legal" style="left:942px">PRIVACY POLICY</div>
  <div class="legal" style="left:1041px">TERMS OF USE</div>
</footer>

</body>
</html>
```